Store Signage for New Location

I need a banner for my new location. It needs to communicate 1: our name, 2: our phone number 3: our message. This is going to be a 7 foot wide banner that is 4 feet tall. It needs to be a very high resolution design so it prints properly.

Our phone number is (913) 548-1907

Our Message: The HONEST alternative to the dealer.

Or: Your Honest Auto Service Center

"Honest" is our key word here.

Target Market(s)

Drive-by traffic.

Industry/Entity Type

Auto Repair

Requirements
Must have
• The name of our business: Tall Pine Auto Repair
• Our phone number: (913) 548-1907
• Our message: The HONEST alternative to the dealership.
• or: Your Honest Service Center
Nice to have
• I really just need a clean layout using the uploaded logo and font. It needs to be highly visible as a sign that is seen by drive-by traffic.
• I'd like the color scheme to be the same as what I have, however, you're more than welcome to add detail and color as needed.

```html
<!DOCTYPE html>
<html lang="en">
<head>
<meta charset="utf-8">
<title>Tall Pine Auto Repair – Store Banner</title>
<link rel="stylesheet" href="https://fonts.googleapis.com/css2?family=Exo+2:ital,wght@0,800;1,700;1,800;1,900&display=swap">
<style>
  :root {
    --stage: #1f1f1f;
    --paper: #f4f4f4;
    --paper-shade: #e6e6e6;
    --charcoal: #343434;
    --orange: #ff7417;
    --ink: #111111;
    --white: #ffffff;
  }
  * { margin: 0; padding: 0; box-sizing: border-box; }
  html, body {
    width: 1200px;
    height: 800px;
    overflow: hidden;
    background: var(--stage);
  }
  .banner {
    position: absolute;
    left: 55px;
    top: 89px;
    width: 1090px;
    height: 622px;
    overflow: hidden;
    background: var(--charcoal);
    font-family: "Exo 2", "Arial Black", sans-serif;
  }
  .banner-shapes {
    position: absolute;
    inset: 0;
  }
  .web-address {
    position: absolute;
    left: 600px;
    top: 34px;
    width: 420px;
    text-align: center;
    font-size: 19px;
    font-weight: 800;
    font-style: italic;
    color: var(--ink);
    letter-spacing: 0.2px;
  }
  .business-name {
    position: absolute;
    left: 288px;
    top: 122px;
    font-size: 43px;
    font-weight: 800;
    color: var(--ink);
    white-space: nowrap;
  }
  .tagline span {
    position: absolute;
    color: var(--white);
    font-style: italic;
    white-space: nowrap;
    line-height: 1;
  }
  .tagline .the { left: 352px; top: 258px; font-size: 62px; font-weight: 800; }
  .tagline .honest { left: 462px; top: 233px; font-size: 138px; font-weight: 900; letter-spacing: 1px; }
  .tagline .alternative { left: 88px; top: 378px; font-size: 52px; font-weight: 700; }
  .tagline .dealer { left: 466px; top: 366px; font-size: 106px; font-weight: 800; }
  .phone-number {
    position: absolute;
    left: 518px;
    top: 513px;
    font-size: 64px;
    font-weight: 800;
    font-style: italic;
    color: var(--white);
    white-space: nowrap;
    line-height: 1;
  }
</style>
</head>
<body>
  <main class="banner">
    <svg class="banner-shapes" width="1090" height="622" viewBox="0 0 1090 622" aria-hidden="false">
      <!-- light header field -->
      <polygon class="header-field" points="0,0 1090,0 1090,137 1010,207 322,207 270,287 0,287" fill="var(--paper)"/>
      <polygon class="header-shade" points="0,230 260,230 230,287 0,287" fill="var(--paper-shade)"/>
      <!-- web address tab -->
      <polygon class="web-tab-edge" points="506,0 522,0 560,75 544,75" fill="var(--ink)"/>
      <polygon class="web-tab" points="522,0 1090,0 1090,75 560,75" fill="var(--orange)"/>
      <!-- name mark -->
      <circle class="name-mark" cx="150" cy="140" r="52" fill="var(--ink)"/>
      <!-- service badges -->
      <g class="service-badges">
        <circle cx="128" cy="500" r="37" fill="var(--white)" stroke="var(--orange)" stroke-width="2" role="img" aria-label="Brake service icon"/>
        <circle cx="230" cy="500" r="37" fill="var(--white)" stroke="var(--orange)" stroke-width="2" role="img" aria-label="Tire service icon"/>
        <circle cx="332" cy="500" r="37" fill="var(--white)" stroke="var(--orange)" stroke-width="2" role="img" aria-label="Oil change icon"/>
      </g>
      <!-- bottom orange band -->
      <polygon class="footer-band" points="0,527 62,527 92,560 420,560 482,494 1032,494 1090,545 1090,622 0,622" fill="var(--orange)"/>
      <!-- phone badge -->
      <g class="phone-badge">
        <circle cx="443" cy="544" r="36" fill="var(--ink)" stroke="var(--orange)" stroke-width="3"/>
        <path d="M433 528 c2 -2 5 -2 6 0 l4 6 c1 2 0 4 -1 5 l-3 2 c2 5 6 9 11 11 l2 -3 c1 -1 3 -2 5 -1 l6 4 c2 1 2 4 0 6 l-3 3 c-3 3 -8 3 -13 0 c-8 -5 -14 -11 -18 -19 c-2 -5 -2 -9 1 -12 z" fill="var(--white)"/>
      </g>
    </svg>

    <div class="web-address">www.TallPineAutoRepair.com</div>
    <div class="business-name">Tall Pine Auto Repair</div>

    <h1 class="tagline">
      <span class="the">The</span>
      <span class="honest">HONEST</span>
      <span class="alternative">alternative to</span>
      <span class="dealer">the dealer</span>
    </h1>

    <div class="phone-number">(913) 548-1907</div>
  </main>
</body>
</html>
```